Senior sex novelty store providing a private method for acquiring the products and knowledge

Our business supplies novelty sex products and services, specializing in the 50+ demographic. Products include sex products for individuals and couples. Services include webinars and teleseminars that address various sex and relationship issues. We are dedicated to providing discreet delivery of products and knowledge to people over 50 entering a new phase of life, facing new challenges. Our entire process from site through shipping is kept private to allow our customers the freedom to shop and learn in the privacy of their own home.

Target Market(s)

Seniors over 50 years old

Industry/Entity Type

Store

Number of Pages Required

1 page

Font styles to use
Serif

Requirements
Must have
• place for business description with a private look
Should not have
• anything sleazy

```html
<!DOCTYPE html>
<html lang="en">
<head>
<meta charset="utf-8">
<title>A Private Shop for Life After 50</title>
<link href="https://fonts.googleapis.com/css2?family=Cormorant+Garamond:wght@300;400;500&family=Lora:wght@400;500;700&display=swap" rel="stylesheet">
<style>
  :root {
    --sky-top: #22bce9;
    --sky-bottom: #168fcf;
    --ink: #1b1b1b;
    --headline: #0e2233;
    --white: #ffffff;
    --plum: #7b1470;
    --badge: #0b3d55;
    --footer: #1a1a1a;
    --partner: #3b3b3b;
    --cart-red: #e0262e;
    --mouse: #0f6fa8;
  }
  * { margin: 0; padding: 0; box-sizing: border-box; }
  html, body { width: 1200px; height: 957px; overflow: hidden; }
  body { font-family: "Lora", Georgia, serif; color: var(--ink); }
  .page { position: relative; width: 1200px; height: 957px; }

  .hero {
    position: absolute; left: 0; top: 0; width: 1200px; height: 806px;
    background: linear-gradient(180deg, var(--sky-top) 0%, var(--sky-bottom) 100%);
  }

  .brand {
    position: absolute; left: 66px; top: 10px;
    font-family: "Lora", Georgia, serif;
    font-size: 50px; font-weight: 400; color: #262626;
  }

  .nav {
    position: absolute; top: 35px; right: 345px;
    display: flex; gap: 32px;
  }
  .nav a {
    font-size: 15px; font-weight: 700; letter-spacing: 0.6px; color: #141414;
    text-decoration: none; text-transform: uppercase;
  }

  .cart-button {
    position: absolute; left: 891px; top: 25px; width: 65px; height: 41px;
    border: 2px solid var(--white); border-radius: 21px;
    display: flex; align-items: center; justify-content: center;
  }
  .cart-count {
    position: absolute; right: -8px; top: -10px; width: 24px; height: 24px;
    border-radius: 50%; background: var(--white); color: var(--cart-red);
    font-size: 14px; font-weight: 700;
    display: flex; align-items: center; justify-content: center;
  }

  .login-button {
    position: absolute; left: 985px; top: 24px; width: 162px; height: 42px;
    border-radius: 21px; background: var(--plum); color: var(--white);
    font-size: 15px; font-weight: 700; letter-spacing: 0.8px;
    display: flex; align-items: center; justify-content: center;
  }

  .hero-photo {
    position: absolute; left: 78px; top: 88px; width: 430px; height: 718px;
    border-radius: 200px 200px 0 0;
    background: linear-gradient(180deg, rgba(30,30,30,0.5) 0%, rgba(40,40,40,0.4) 32%, rgba(245,247,250,0.85) 50%, rgba(240,222,208,0.7) 80%, rgba(232,208,192,0.55) 100%);
  }

  .price-badge { position: absolute; left: 380px; top: 387px; width: 214px; height: 214px; }
  .price-badge .price {
    position: absolute; inset: 0;
    display: flex; align-items: center; justify-content: center;
    color: var(--white); font-size: 56px; font-weight: 500;
  }

  .headline {
    position: absolute; left: 614px; top: 214px;
    font-family: "Cormorant Garamond", Georgia, serif;
    font-size: 54px; font-weight: 300; line-height: 74px; letter-spacing: 2px;
    color: var(--headline); text-transform: uppercase;
  }

  .intro {
    position: absolute; left: 615px; top: 390px; width: 530px;
    font-size: 20px; font-weight: 400; line-height: 34.7px; color: var(--white);
  }

  .actions { position: absolute; left: 615px; top: 542px; display: flex; gap: 33px; }
  .btn {
    height: 58px; border-radius: 29px;
    font-size: 15px; font-weight: 700; letter-spacing: 0.6px;
    display: flex; align-items: center; justify-content: center; text-transform: uppercase;
  }
  .btn-cart { width: 197px; background: var(--white); color: var(--plum); }
  .btn-description { width: 185px; background: var(--ink); color: var(--white); }

  .scroll-hint { position: absolute; left: 589px; top: 692px; }

  .partners {
    position: absolute; left: 0; top: 806px; width: 1200px; height: 151px;
    background: var(--footer);
    display: flex; align-items: center; justify-content: space-between;
    padding: 0 80px 0 74px;
  }
  .partners span { font-size: 28px; font-weight: 700; color: var(--partner); }
</style>
</head>
<body>
<div class="page">
  <section class="hero">
    <div class="brand">Logo</div>
    <nav class="nav">
      <a href="#">Catalog</a>
      <a href="#">Popular</a>
      <a href="#">Information</a>
    </nav>
    <div class="cart-button">
      <svg width="18" height="16" viewBox="0 0 18 16" aria-hidden="true">
        <path d="M1 2h3l2 8h9l2-6H5" fill="none" stroke="#fff" stroke-width="2" stroke-linejoin="round"/>
        <path d="M5 4h12l-2 6H6z" fill="#fff"/>
        <circle cx="7" cy="13.5" r="1.5" fill="#fff"/>
        <circle cx="14" cy="13.5" r="1.5" fill="#fff"/>
      </svg>
      <span class="cart-count">2</span>
    </div>
    <div class="login-button">LOG IN</div>

    <div class="hero-photo" role="img" aria-label="Product photo of a woman with long dark hair in a white satin nightdress"></div>

    <div class="price-badge">
      <svg width="214" height="214" viewBox="0 0 214 214" aria-hidden="true">
        <circle cx="107" cy="107" r="104" fill="none" stroke="#fff" stroke-width="2" stroke-dasharray="7 5"/>
        <circle cx="107" cy="107" r="98" fill="var(--badge)"/>
      </svg>
      <div class="price">$400</div>
    </div>

    <h1 class="headline">A Private Shop<br>For Life After 50</h1>
    <p class="intro">Thoughtful products, webinars and teleseminars for people over 50, chosen with care and shipped in plain packaging. Private from first click to your door.</p>

    <div class="actions">
      <div class="btn btn-cart">Add to my cart</div>
      <div class="btn btn-description">Description</div>
    </div>

    <svg class="scroll-hint" width="28" height="44" viewBox="0 0 28 44" aria-hidden="true">
      <rect x="2" y="2" width="24" height="40" rx="12" fill="none" stroke="var(--mouse)" stroke-width="2"/>
      <line x1="14" y1="9" x2="14" y2="15" stroke="var(--mouse)" stroke-width="2"/>
    </svg>
  </section>

  <footer class="partners">
    <span>Northvale Works</span>
    <span>Ardenly</span>
    <span>Colbrith</span>
    <span>Tavrin</span>
    <span>Kestova</span>
    <span>Ardenly</span>
  </footer>
</div>
</body>
</html>
```